Brambleton Resource Holdings, LP Letter Head

We need an official company letter head design that is clean and mimics our company logo style. It will include our logo, address, phone, and website. We are an OIl and Gas mineral purchasing company, so hints of oil rigs or related design would be desirable.

Industry/Entity Type

Oil And Gas

Colors
ec1f27
f04a50
f59195
fbd4d5

Requirements
Must have
• Logo
• 7392 Whitcombe R. Ashdale Parkway, Suite 618
• Dallas TX, 75391
• 214-673-1958
• www.bramblestoneres.example
Nice to have
• Oil Rigs or OIl and gas related design

```html
<!DOCTYPE html>
<html lang="en">
<head>
<meta charset="utf-8">
<title>Brambleton Resource Holdings – Letterhead</title>
<link rel="stylesheet" href="https://fonts.googleapis.com/css2?family=Cinzel:wght@600&family=Roboto:wght@500&display=swap">
<style>
  :root {
    --brand-red: #ec1f27;
    --paper: #ffffff;
    --backdrop: #e4eaea;
    --footer-text: #ffffff;
  }
  * { margin: 0; padding: 0; box-sizing: border-box; }
  html, body {
    width: 1131px;
    height: 1200px;
    overflow: hidden;
    background: var(--backdrop);
  }
  .letterhead {
    position: absolute;
    left: 140px;
    top: 50px;
    width: 850px;
    height: 1100px;
    background: var(--paper);
    box-shadow: 0 4px 14px rgba(0,0,0,0.18);
    overflow: hidden;
  }
  .brand-mark {
    position: absolute;
    left: 40px;
    top: 34px;
    width: 58px;
    height: 58px;
    background: var(--brand-red);
  }
  .header-graphics {
    position: absolute;
    left: 0;
    top: 0;
    width: 850px;
    height: 110px;
  }
  .company-name {
    position: absolute;
    right: 40px;
    top: 62px;
    font-family: "Cinzel", serif;
    font-weight: 600;
    color: var(--brand-red);
    text-align: right;
    white-space: nowrap;
    line-height: 1;
  }
  .company-name .name-main {
    display: block;
    font-size: 28px;
    letter-spacing: 0.5px;
  }
  .company-name .name-sub {
    display: block;
    margin-top: 4px;
    font-size: 12px;
    letter-spacing: 3px;
  }
  .letter-footer {
    position: absolute;
    left: 0;
    bottom: 0;
    width: 100%;
    height: 200px;
    background: var(--brand-red);
    padding: 22px 40px 0;
    font-family: "Roboto", sans-serif;
    font-weight: 500;
    font-size: 14px;
    color: var(--footer-text);
  }
  .contact-row {
    display: flex;
    align-items: center;
    gap: 8px;
    height: 22px;
  }
  .contact-row.website { margin-left: 120px; margin-top: 6px; }
  .contact-icon { width: 14px; height: 14px; flex: none; }
</style>
</head>
<body>
  <main class="letterhead">
    <div class="brand-mark" aria-hidden="true"></div>

    <svg class="header-graphics" viewBox="0 0 850 110" aria-hidden="true">
      <polygon points="70,22 810,22 790,54 116,54" fill="var(--brand-red)"/>
      <rect x="116" y="90" width="420" height="4" fill="var(--brand-red)"/>
    </svg>

    <div class="company-name">
      <span class="name-main">Brambleton</span>
      <span class="name-sub">Resource Holdings</span>
    </div>

    <footer class="letter-footer">
      <div class="contact-row address">
        <svg class="contact-icon" viewBox="0 0 16 16" aria-hidden="true">
          <path d="M2 8 L8 2 L14 8 M4 7 V14 H12 V7" fill="none" stroke="#fff" stroke-width="1.6"/>
          <rect x="7" y="10" width="2" height="4" fill="#fff"/>
        </svg>
        <span>7392 Whitcombe R. Ashdale Parkway, Suite 618 Dallas TX, 75391</span>
      </div>
      <div class="contact-row phone">
        <svg class="contact-icon" viewBox="0 0 16 16" aria-hidden="true">
          <rect x="4" y="1" width="8" height="14" rx="1.5" fill="none" stroke="#fff" stroke-width="1.6"/>
          <rect x="6.5" y="12" width="3" height="1.4" fill="#fff"/>
        </svg>
        <span>214-673-1958</span>
      </div>
      <div class="contact-row website">
        <svg class="contact-icon" viewBox="0 0 16 16" aria-hidden="true">
          <circle cx="8" cy="8" r="6.5" fill="none" stroke="#fff" stroke-width="1.4"/>
          <ellipse cx="8" cy="8" rx="3" ry="6.5" fill="none" stroke="#fff" stroke-width="1.2"/>
          <line x1="1.5" y1="8" x2="14.5" y2="8" stroke="#fff" stroke-width="1.2"/>
        </svg>
        <span>www.bramblestoneres.example</span>
      </div>
    </footer>
  </main>
</body>
</html>
```